Kestrel Summit 2019 Enemies of the End-Times Church Flyer

We want a church conference flyer designed. We are looking for a professional, yet catchy design that uses our brand colors and logo creatively while communicating key information of the event effectively. <br/>The flyer must include all of the following:<br/>Title: Kestrel Summit 2019<br/>Topic: The Enemies of The End-Times Church <br/>Subtitles: <br/> -How the antichrist raises an army by social behavior engineering. <br/>-How the architects of modern social constructs escaped the church's radar. <br/>-The Holy Spirit's end-times agenda:<br/> The Knock-Out Punch!<br/>Speaker: Prophet Marcus Toliver <br/>Dates/time: December 27, 28 & 29 at 6pm<br/>Location: Halvorn Community Center <br/> 241 Pellham Street <br/> Portland, ME 04102<br/>Contact info: phone: 207-555-0148 <br/>email: contact@brookmeadow.example <br/> www.vutel.example<br/>*The flyer must also include a picture of the speaker and our Vutel logo <br/>Thanks, we look forward to seeing what you come up with!

Colors

Designer to choose colors to be used in the design.

Requirements
Must have
• The flyer must include all of the following:
• Title: Kestrel Summit 2019
• Topic: The Enemies of The End-Times Church
• Subtitles:
• -How the antichrist raises an army by social behavior engineering.
• -How the architects of modern social constructs escaped the church's radar.
• -The Holy Spirit's end-times agenda:
• The Knock-Out Punch!
• Speaker: Prophet Marcus Toliver
• Dates/time: December 27, 28 & 29 at 6pm
• Location: Halvorn Community Center
• 241 Pellham Street
• Portland, ME 04102
• Contact info: phone: 207-555-0148
• email: contact@brookmeadow.example
• www.vutel.example
• *The flyer must also include a picture of the speaker and our Vutel logo
Should not have
• Pictures of crosses or church buildings

```html
<!DOCTYPE html>
<html lang="en">
<head>
<meta charset="utf-8">
<title>Kestrel Summit 2019 Flyer</title>
<link rel="stylesheet" href="https://fonts.googleapis.com/css2?family=Exo+2:wght@600;700;800&family=Oswald:wght@500;600&family=Barlow+Semi+Condensed:wght@400;500;600&display=swap">
<style>
  :root {
    --page-bg: #d7d7d7;
    --navy: #0b3a52;
    --navy-mid: #16323f;
    --night: #0e0e0f;
    --orange: #f7931e;
    --white: #ffffff;
    --silver: #b9bcbf;
    --ink: #1c1c1c;
  }
  * { box-sizing: border-box; margin: 0; padding: 0; }
  html, body { width: 703px; height: 1200px; overflow: hidden; }
  body { background: var(--page-bg); font-family: "Barlow Semi Condensed", sans-serif; position: relative; }

  .flyer {
    position: absolute; left: 21px; top: 134px; width: 660px; height: 932px;
    background: linear-gradient(180deg, var(--navy) 0%, var(--navy-mid) 38%, #121a1f 68%, var(--night) 100%);
    box-shadow: 0 6px 18px rgba(0,0,0,.35);
    overflow: hidden; color: var(--white);
  }
  .abs { position: absolute; }

  .metal {
    background: linear-gradient(180deg, #ffffff 0%, #ffffff 45%, var(--silver) 70%, #ffffff 100%);
    -webkit-background-clip: text; background-clip: text; color: transparent;
  }

  .title { left: 93px; width: 478px; text-align: center; line-height: 1; font-family: "Exo 2", sans-serif; font-weight: 800; }
  .title-line1 { top: 38px; display: flex; justify-content: center; align-items: baseline; gap: 12px; }
  .title-name { font-size: 70px; letter-spacing: 1px; }
  .title-year { font-family: "Oswald", sans-serif; font-weight: 600; font-size: 82px; color: var(--orange); line-height: .9; }
  .title-line2 { top: 120px; font-size: 84px; letter-spacing: 18px; padding-left: 18px; }

  .dates { left: 93px; top: 206px; width: 478px; display: flex; justify-content: space-between; align-items: center; }
  .dates-day { font-family: "Exo 2", sans-serif; font-weight: 700; font-size: 40px; color: var(--orange); letter-spacing: 1px; line-height: 1; }
  .dates-time {
    background: linear-gradient(180deg, #ffffff, #dcdcdc); color: var(--ink);
    font-family: "Oswald", sans-serif; font-weight: 500; font-size: 38px; line-height: 47px;
    width: 121px; text-align: center;
  }

  .topic {
    left: 93px; top: 260px; width: 478px; height: 45px; background: var(--orange);
    color: var(--ink); font-family: "Exo 2", sans-serif; font-weight: 700; font-size: 19px;
    display: flex; align-items: center; justify-content: center; letter-spacing: .3px;
  }

  .subtopics { left: 93px; top: 314px; width: 478px; display: flex; align-items: center; gap: 22px; font-size: 13.5px; line-height: 1.08; font-weight: 500; }
  .subtopics p { flex: 1; }
  .subtopics p + .divider + p { flex: 1.12; }
  .subtopics .divider { width: 1.5px; height: 30px; background: var(--white); flex: none; }

  .speaker-art { left: 0; top: 377px; width: 340px; height: 555px; }

  .agenda-lead { left: 314px; top: 418px; font-size: 16px; font-weight: 400; }
  .agenda-punch { left: 314px; top: 438px; font-family: "Exo 2", sans-serif; font-weight: 700; font-size: 20px; color: var(--orange); letter-spacing: .5px; }
  .speaker-title { left: 312px; top: 462px; font-family: "Oswald", sans-serif; font-weight: 600; line-height: 1; }
  .speaker-role { font-size: 80px; display: block; letter-spacing: -1px; }
  .speaker-name { font-size: 48px; display: block; margin-top: 0; letter-spacing: -.5px; white-space: nowrap; }

  .brand { left: 392px; top: 716px; display: flex; align-items: center; gap: 10px; }
  .brand-dot { width: 18px; height: 18px; border-radius: 50%; background: var(--orange); }
  .brand-name { font-weight: 500; font-size: 46px; letter-spacing: 2px; color: var(--white); line-height: 1; }

  .contact { left: 386px; top: 796px; font-size: 12px; line-height: 1.12; font-style: normal; }
  .contact-row { display: flex; align-items: flex-start; gap: 6px; margin-bottom: 6px; }
  .contact-row svg { width: 13px; height: 13px; flex: none; margin-top: 1px; }
  .contact-phone { font-size: 18px; font-weight: 500; }
  .contact-phone svg { margin-top: 4px; }
</style>
</head>
<body>
  <main class="flyer">
    <div class="abs title title-line1">
      <span class="metal title-name">KESTREL</span>
      <span class="title-year">2019</span>
    </div>
    <div class="abs title title-line2 metal">SUMMIT</div>

    <div class="abs dates">
      <span class="dates-day">DECEMBER 27-29</span>
      <span class="dates-time">AT 6PM</span>
    </div>

    <div class="abs topic">TOPIC: THE ENEMIES OF THE END-TIMES CHURCH</div>

    <div class="abs subtopics">
      <p>How the antichrist raises an army by social behavior engineering</p>
      <span class="divider"></span>
      <p>How the architects of modern social constructs escaped the church's radar</p>
    </div>

    <svg class="abs speaker-art" viewBox="0 0 340 555" aria-hidden="false">
      <defs>
        <radialGradient id="photoTone" cx="40%" cy="30%" r="75%">
          <stop offset="0" stop-color="#4a3a33"/>
          <stop offset=".4" stop-color="#3a3b3e"/>
          <stop offset="1" stop-color="#232427"/>
        </radialGradient>
      </defs>
      <path class="flame-curve" d="M200 0 C275 40 262 150 205 225 C300 280 345 380 322 470 C310 520 290 545 275 555 L180 555 Z" fill="var(--orange)"/>
      <path role="img" aria-label="Photo of speaker Prophet Marcus Toliver in a grey blazer over a red zip top"
            d="M70 20 C80 0 200 0 222 25 L228 200 C262 225 282 300 292 420 L305 555 L0 555 L0 260 C20 230 50 215 62 205 Z"
            fill="url(#photoTone)"/>
    </svg>

    <p class="abs agenda-lead">The Holy Spirit's end-times agenda:</p>
    <p class="abs agenda-punch">THE KNOCK-OUT PUNCH!</p>
    <h2 class="abs speaker-title">
      <span class="speaker-role metal">PROPHET</span>
      <span class="speaker-name metal">MARCUS TOLIVER</span>
    </h2>

    <div class="abs brand">
      <span class="brand-dot"></span>
      <span class="brand-name">VUTEL</span>
    </div>

    <address class="abs contact">
      <div class="contact-row contact-phone">
        <svg viewBox="0 0 24 24"><path d="M6.6 10.8a15 15 0 0 0 6.6 6.6l2.2-2.2a1 1 0 0 1 1-.25 11 11 0 0 0 3.6.6 1 1 0 0 1 1 1V20a1 1 0 0 1-1 1A17 17 0 0 1 3 4a1 1 0 0 1 1-1h3.5a1 1 0 0 1 1 1 11 11 0 0 0 .6 3.6 1 1 0 0 1-.25 1z" fill="var(--orange)"/></svg>
        <span>207-555-0148</span>
      </div>
      <div class="contact-row">
        <svg viewBox="0 0 24 24"><path d="M12 2a7 7 0 0 0-7 7c0 5 7 13 7 13s7-8 7-13a7 7 0 0 0-7-7zm0 9.5A2.5 2.5 0 1 1 12 6.5a2.5 2.5 0 0 1 0 5z" fill="var(--orange)"/></svg>
        <span>Halvorn Community Center<br>241 Pellham Street Portland,<br>ME 04102</span>
      </div>
      <div class="contact-row">
        <svg viewBox="0 0 24 24"><rect x="2" y="5" width="20" height="14" fill="var(--orange)"/><path d="M2 5l10 8 10-8" stroke="var(--night)" stroke-width="1.8" fill="none"/></svg>
        <span>contact@brookmeadow.example</span>
      </div>
      <div class="contact-row">
        <svg viewBox="0 0 24 24"><circle cx="12" cy="12" r="10" fill="var(--orange)"/><path d="M2 12h20M12 2c3 3 3 17 0 20M12 2c-3 3-3 17 0 20" stroke="var(--night)" stroke-width="1.5" fill="none"/></svg>
        <span>www.vutel.example</span>
      </div>
    </address>
  </main>
</body>
</html>
```